Kitchen and bathroom exhaust fan cleaning business card design

A new business cleaning domestic - not commercial - exhaust/extractor fans in kitchens, bathrooms and en suites and kitchen range hood filters.

We would like a bright colour suggesting cleanliness (such a syellow or light green?)

I would like to see on the card preferably on the reverse:

"We clean kitchen and bathroom exhaust fans & Volrex Brightos
and
clean and repair range hood filters and replace carbon filters

We give Pensioner discounts
Updates

Designers pls note the TM in the contact filed after Pureflow Vents should be superscript as in the trademark sign. On the reverse of the card, I would like:: "We clean kitchen and bathroom exhaust fans & Volrex Brightos & clean and repair range hood filters and replace carbon filters We give Pensioner discounts

Reason: I will be out of the country for several days

Target Market(s)

people who are too lazy or too busy to clean their fan units and pensioners and others who are unable to do it.

Industry/Entity Type

Business

Contact Information for Business Card

ACT Clean FansTM Designer pls note the TM should be superscript as in the trademark sign
Neil Oakley
Mob: 0431 572 864
Email: pureflowvents@zentromail.com
PO Box 7152, Pellow ACT 2608

Requirements
Must have
• Designer pls note the TM in the contact filed after Pureflow Vents should be superscript as in the trademark sign.

On the reverse

and

```html
<!DOCTYPE html>
<html lang="en">
<head>
<meta charset="utf-8">
<title>Pureflow Vents – Business Card</title>
<link rel="stylesheet" href="https://fonts.googleapis.com/css2?family=Anton&family=Arimo:ital,wght@0,400;0,700;1,700&display=swap">
<style>
  :root {
    --yellow: #f8ee45;
    --yellow-deep: #d9cf1c;
    --green: #43ad4a;
    --white: #ffffff;
    --ink: #111111;
    --dot: #f3ec52;
  }
  html, body {
    margin: 0;
    padding: 0;
    overflow: hidden;
  }
  body {
    width: 1200px;
    height: 965px;
    background: var(--white);
    position: relative;
    font-family: "Arimo", Arial, sans-serif;
  }
  .card {
    position: absolute;
    width: 482px;
    height: 297px;
    overflow: hidden;
  }
  .card--front { left: 92px; top: 320px; }
  .card--back  { left: 631px; top: 321px; }

  .card__art {
    position: absolute;
    inset: 0;
    width: 100%;
    height: 100%;
  }

  /* Front */
  .brand {
    margin: 0;
    color: var(--white);
    font-family: "Anton", "Arial Narrow", sans-serif;
    font-weight: 400;
    text-transform: uppercase;
  }
  .brand__main {
    position: absolute;
    left: 178px;
    top: 14px;
    font-size: 72px;
    line-height: 1;
    letter-spacing: 0;
    white-space: nowrap;
    transform: scaleY(2.3);
    transform-origin: left top;
  }
  .brand__sub {
    position: absolute;
    left: 180px;
    top: 240px;
    font-size: 34px;
    line-height: 1;
    letter-spacing: 24px;
    white-space: nowrap;
  }
  .brand__tm {
    font-size: 0.45em;
    vertical-align: super;
    letter-spacing: 0;
    margin-left: -18px;
  }

  /* Back */
  .services {
    position: absolute;
    left: 24px;
    top: 55px;
    margin: 0;
    padding: 0;
    list-style: none;
    color: var(--white);
    font-style: italic;
    font-weight: 700;
    font-size: 15.5px;
    line-height: 25.5px;
  }
  .services__item {
    position: relative;
    padding-left: 13px;
  }
  .services__item::before {
    content: "";
    position: absolute;
    left: 0;
    top: 11px;
    width: 7px;
    height: 7px;
    border-radius: 50%;
    background: var(--dot);
  }
  .services__cont {
    display: block;
    padding-left: 2px;
  }
  .contact {
    position: absolute;
    left: 26px;
    top: 172px;
    margin: 0;
    color: var(--white);
    font-style: normal;
    font-weight: 700;
    font-size: 15.5px;
    line-height: 27px;
  }
  .badge {
    position: absolute;
    left: 300px;
    top: 36px;
    width: 134px;
    height: 134px;
    border-radius: 50%;
    background: var(--green);
    box-shadow: 0 0 0 2px var(--yellow);
    display: flex;
    align-items: center;
    justify-content: center;
  }
  .badge__text {
    margin: 0;
    transform: rotate(-11deg);
    color: var(--white);
    font-weight: 700;
    font-size: 18px;
    line-height: 21px;
    text-align: center;
    text-transform: uppercase;
  }

  .side-label {
    position: absolute;
    top: 651px;
    margin: 0;
    color: var(--ink);
    font-family: "Arimo", Arial, sans-serif;
    font-size: 20px;
    font-weight: 400;
    transform: translateX(-50%);
  }
  .side-label--front { left: 333px; }
  .side-label--back  { left: 872px; }
</style>
</head>
<body>

  <section class="card card--front" aria-label="Card front">
    <svg class="card__art" viewBox="0 0 482 297" aria-hidden="true">
      <defs>
        <radialGradient id="fanGlow" cx="0.3" cy="0.85" r="0.9">
          <stop offset="0" stop-color="#f8ee45"/>
          <stop offset="0.6" stop-color="#e6dc2a"/>
          <stop offset="1" stop-color="#f8ee45"/>
        </radialGradient>
      </defs>
      <rect width="482" height="297" fill="url(#fanGlow)" role="img" aria-label="Close-up of a round exhaust fan grille in yellow"/>
      <path d="M103 297 C 110 225, 165 170, 240 165 L482 165 L482 297 Z" fill="var(--green)"/>
    </svg>
    <h1 class="brand">
      <span class="brand__main">Pureflow</span>
      <span class="brand__sub">Vents<span class="brand__tm">™</span></span>
    </h1>
  </section>

  <section class="card card--back" aria-label="Card back">
    <svg class="card__art" viewBox="0 0 482 297" aria-hidden="true">
      <defs>
        <linearGradient id="ventGlow" x1="0" y1="0" x2="1" y2="1">
          <stop offset="0" stop-color="#f8ee45"/>
          <stop offset="0.5" stop-color="#e8de2d"/>
          <stop offset="1" stop-color="#f8ee45"/>
        </linearGradient>
      </defs>
      <rect width="482" height="297" fill="url(#ventGlow)" role="img" aria-label="Square ceiling exhaust vent grille in yellow"/>
      <path d="M0 0 L160 0 C 265 5, 335 75, 335 165 L335 297 L0 297 Z" fill="var(--green)"/>
    </svg>

    <ul class="services">
      <li class="services__item">we clean kitchen &amp; bathroom
        <span class="services__cont">exhaust fans &amp; Volrex Brightos</span></li>
      <li class="services__item">clean &amp; repair range hood filters</li>
      <li class="services__item">replace carbon filters</li>
    </ul>

    <address class="contact">
      Neil Oakley<br>
      Mob: 0431 572 864<br>
      Email: pureflowvents@zentromail.com<br>
      PO Box 7152, Pellow ACT 2608
    </address>

    <div class="badge">
      <p class="badge__text">We give<br>pensioner<br>discounts</p>
    </div>
  </section>

  <p class="side-label side-label--front">FRONT</p>
  <p class="side-label side-label--back">BACK</p>

</body>
</html>
```